International oil and gas consultancy business needs a web design

Hello, I need a web design for a new oil and gas auditing consultancy business. My business undertakes contract audit assignments to review past costs of oil and gas operations (see attached Excel file for more details of the businesses services). I need the design to give the impression of a professional consultancy style of business, rather than a retail style of website. Note: this job is for LAYOUT DESIGN ONLY and not coding / development work.
The following are my key design principles:
1. BASIC DESIGN: I am after a simple and static web design. I don't want the pages busy or cluttered with too many images or detail.
2. HORIZONTAL TABS: I require a horizontal set of tabs towards the top of the screens (see Excel file) which remain in the same position on every page.
3. META TAG PLANNING: The design should allow for effective positioning of content so that key meta tag words can easily be built during the technical build stage.
4. NUMBER OF PAGES: The site will eventually have a maximum of 10 pages. Seven of the pages will reside under the tabs. Can you please present your opening submission for the first two page.
5. USE OF MY LOGO: The attached logo (JPEG file) should be used throughout the website. Please don't change the shape and colour.
6. COLOUR SCHEMES: Can you please consider any of the 3 colour schemes below:
A - dark red (to match the logo), light grey and perhaps another of your liking;
B - dark red (to match the logo), light cream and perhaps another of your liking;
C - dark red (to match the logo), white and perhaps another of your liking.
7. WORD CONTENT: I have attached an Excel file which shows the estimated word content for each page.
8. FUTURE USE OF DESIGN: I'm planning on building a Wordpress website. Can you please ensure the layout design supports this application.

Target Market(s)

oil and gas companies (small and large)

Industry/Entity Type

Oil And Gas

Font styles to use
Sans Serif

Requirements
Nice to have
• The KOL logo and business name should ideally be next to each other. Also, the logo and name should be part of the background graphics, not above it.

```html
<!DOCTYPE html>
<html lang="en">
<head>
<meta charset="utf-8">
<title>KOL – Kestrel Oilfield Ledgers</title>
<link href="https://fonts.googleapis.com/css2?family=Roboto:wght@400;500;700&family=Lato:wght@400;700&display=swap" rel="stylesheet">
<style>
  :root{
    --brand-red:#7d0e1a;
    --brand-red-dark:#5c0912;
    --nav-top:#6b6b6b;
    --nav-bottom:#2c2c2c;
    --text:#3c3c3c;
    --muted:#e6e6e6;
    --rule:#d6d6d6;
    --white:#ffffff;
    --footer:#3a3a3a;
  }
  *{box-sizing:border-box;margin:0;padding:0}
  html,body{width:1200px;height:1164px;overflow:hidden;background:var(--white)}
  body{font-family:"Lato",sans-serif;color:var(--text)}
  .page{position:relative;width:1300px;height:1261px;transform:scale(0.923077);transform-origin:0 0}

  .brand{position:absolute;left:95px;top:18px}
  .brand-mark{display:flex;align-items:center;gap:10px}
  .brand-square{width:14px;height:14px;background:var(--brand-red)}
  .brand-name{font-family:"Roboto",sans-serif;font-weight:700;font-size:44px;color:var(--brand-red);line-height:52px;letter-spacing:2px}
  .brand-full{font-family:"Roboto",sans-serif;font-size:14px;color:#222;margin-top:4px}

  .main-nav{position:absolute;left:80px;top:113px;width:1140px;height:57px;border-radius:4px 4px 0 0;
    background:linear-gradient(var(--nav-top),#3d3d3d 60%,var(--nav-bottom));display:flex;align-items:center}
  .main-nav a{font-family:"Roboto",sans-serif;font-size:15px;color:var(--white);text-decoration:none;letter-spacing:.4px;
    height:57px;line-height:57px;padding:0 31px}
  .main-nav a.active{background:linear-gradient(#9b1c28,var(--brand-red));border-radius:4px 0 0 0;width:102px;padding:0;text-align:center;margin-right:2px}

  .hero{position:absolute;left:80px;top:170px;width:1140px;height:536px;
    background:radial-gradient(ellipse at 35% 45%,#f6a13a 0%,#e2642a 30%,#a33a2a 60%,#2a1d24 100%)}
  .hero-copy{position:absolute;left:604px;top:120px;color:var(--white);width:450px}
  .hero-title{font-family:"Lato",sans-serif;font-size:36px;font-weight:400;letter-spacing:.5px;line-height:48px}
  .hero-text{font-size:20px;line-height:33px;letter-spacing:.8px;margin-top:4px;text-align:justify}
  .slider-dots{position:absolute;left:535px;top:508px;display:flex;gap:8px}
  .slider-dots span{width:11px;height:11px;border-radius:50%;background:#9a9a9a}
  .slider-dots span.on{background:var(--white)}

  .btn-more{display:flex;width:150px;height:32px;text-decoration:none}
  .btn-more .label{flex:1;background:var(--muted);color:var(--brand-red);font-family:"Roboto",sans-serif;font-size:13px;letter-spacing:.5px;line-height:32px;text-align:center}
  .btn-more .arrow{width:30px;background:var(--brand-red);display:flex;align-items:center;justify-content:center}
  .hero .btn-more{margin-top:12px;margin-left:1px}
  .hero .btn-more .label{color:#555}

  .services-heading{position:absolute;left:0;top:736px;width:1300px;text-align:center;font-family:"Roboto",sans-serif;font-size:22px;color:var(--brand-red)}
  .service{position:absolute;top:792px;width:358px;height:60px;background:var(--brand-red);border-bottom:3px solid #b01a28;
    display:flex;align-items:center;justify-content:space-between;padding:0 16px 0 26px;color:var(--white);
    font-family:"Roboto",sans-serif;font-size:20px;letter-spacing:1.2px;text-decoration:none}
  .service:nth-of-type(1){left:80px}
  .service:nth-of-type(2){left:472px;padding-left:34px}
  .service:nth-of-type(3){left:862px;padding-left:31px}

  .rule{position:absolute;top:897px;height:1px;background:var(--rule)}
  .rule.left{left:80px;width:848px}
  .rule.right{left:958px;width:262px}

  .city-photo{position:absolute;left:80px;top:930px;width:293px;height:195px;background:linear-gradient(#2f5fb8 0%,#5a8fd6 55%,#1e3f6e 78%,#173050 100%)}
  .section-title{font-family:"Roboto",sans-serif;font-size:20px;color:var(--brand-red);letter-spacing:.5px;font-weight:400}
  .who{position:absolute;left:400px;top:926px;width:525px}
  .who p{font-size:13.5px;line-height:23px;margin-top:10px;color:#555}
  .who .btn-more{position:absolute;top:168px}
  .why{position:absolute;left:958px;top:926px;width:270px}
  .why ul{list-style:none;margin-top:10px}
  .why li{font-size:13.5px;line-height:31px;color:#555;padding-left:24px;position:relative;white-space:nowrap}
  .why li::before{content:"";position:absolute;left:0;top:12px;width:6px;height:6px;border-radius:50%;background:var(--brand-red)}
  .why .btn-more{position:absolute;top:168px}

  .site-footer{position:absolute;left:0;top:1166px;width:1300px;height:95px;background:linear-gradient(#4a4a4a,#2f2f2f)}
  .footer-nav{position:absolute;left:85px;top:25px;font-family:"Roboto",sans-serif;font-size:12.5px;color:var(--white)}
  .footer-nav a{color:var(--white);text-decoration:none}
  .footer-nav .sep{margin:0 7px}
  .copyright{position:absolute;left:85px;top:54px;font-size:12.5px;color:#e0e0e0}
</style>
</head>
<body>
<div class="page">
  <header class="brand">
    <div class="brand-mark"><span class="brand-name">KOL</span><span class="brand-square"></span></div>
    <div class="brand-full">Kestrel Oilfield Ledgers</div>
  </header>

  <nav class="main-nav">
    <a class="active" href="#">HOME</a>
    <a href="#">ABOUT US</a>
    <a href="#">SERVICES</a>
    <a href="#">OUR PARTNERS</a>
    <a href="#">APPROACH</a>
    <a href="#">WHY CHOOSE US</a>
    <a href="#">CONTACT US</a>
  </nav>

  <section class="hero" role="img" aria-label="Silhouettes of two engineers in hard hats shaking hands in front of an offshore oil platform at sunset">
    <div class="hero-copy">
      <h1 class="hero-title">Kestrel Oilfield Ledgers</h1>
      <p class="hero-text">is an Australian based consultancy firm that specialises in providing quality audit services for the oil and gas industry</p>
      <a class="btn-more" href="#"><span class="label">LEARN MORE</span><span class="arrow"><svg width="10" height="12" viewBox="0 0 10 12"><path d="M3 1l5 5-5 5" fill="none" stroke="#fff" stroke-width="2"/></svg></span></a>
    </div>
    <div class="slider-dots"><span class="on"></span><span></span><span></span><span></span></div>
  </section>

  <h2 class="services-heading">Kestrel Oilfield Ledgers specialise in the following services:</h2>
  <a class="service" href="#">JOINT&nbsp; VENTURE&nbsp; AUDITS<svg width="20" height="20" viewBox="0 0 20 20"><circle cx="10" cy="10" r="9.5" fill="#fff"/><path d="M8 6l5 4-5 4z" fill="#444"/></svg></a>
  <a class="service" href="#">CONTRACT AUDITS<svg width="20" height="20" viewBox="0 0 20 20"><circle cx="10" cy="10" r="9.5" fill="#fff"/><path d="M8 6l5 4-5 4z" fill="#444"/></svg></a>
  <a class="service" href="#">OPERATIONS AUDITS<svg width="20" height="20" viewBox="0 0 20 20"><circle cx="10" cy="10" r="9.5" fill="#fff"/><path d="M8 6l5 4-5 4z" fill="#444"/></svg></a>

  <div class="rule left"></div>
  <div class="rule right"></div>

  <div class="city-photo" role="img" aria-label="City skyline with office towers beside a river under a blue sky"></div>

  <section class="who">
    <h3 class="section-title">WHO WE ARE</h3>
    <p>Kestrel Oilfield Ledgers, trading as Kestrel Oilfield Ledgers Pty Ltd, is incorporated and based in Perth, Western Australia. The firm was founded in 2014 by Ray Dunmore. Ray has over 20 years of diverse accounting, project and operational experience. Starting out as an auditor in public practice, Ray moved into commerce and held CFO, COO and many EPC project (construction) finance positions.</p>
    <a class="btn-more" href="#"><span class="label">LEARN MORE</span><span class="arrow"><svg width="10" height="12" viewBox="0 0 10 12"><path d="M3 1l5 5-5 5" fill="none" stroke="#fff" stroke-width="2"/></svg></span></a>
  </section>

  <section class="why">
    <h3 class="section-title">WHY CHOOSE US</h3>
    <ul>
      <li>Cost savings</li>
      <li>Risk Mitigation</li>
      <li>Process Improvement</li>
      <li>Contractual Efficiency &amp; Effrectiveness</li>
    </ul>
    <a class="btn-more" href="#"><span class="label">LEARN MORE</span><span class="arrow"><svg width="10" height="12" viewBox="0 0 10 12"><path d="M3 1l5 5-5 5" fill="none" stroke="#fff" stroke-width="2"/></svg></span></a>
  </section>

  <footer class="site-footer">
    <nav class="footer-nav">
      <a href="#">HOME</a><span class="sep">/</span><a href="#">ABOUT US</a><span class="sep">/</span><a href="#">SERVICES</a><span class="sep">/</span><a href="#">OUR PARTNERS</a><span class="sep">/</span><a href="#">APPROACH</a><span class="sep">/</span><a href="#">WHY CHOOSE US</a><span class="sep">/</span><a href="#">CONTACT US</a>
    </nav>
    <p class="copyright">© 2014 KOL All right reserved</p>
  </footer>
</div>
</body>
</html>
```